We require a banner design for a 53' x 10' trailer for a future development to be displayed on the side of the highway. The development name is 712 35 Commerce Park, logo is attached. This is an industrial future development. Please also include the RLW Group logo and MERO Development logos as well.

Industry/Entity Type

Real Estate / Construction / Developer / Industrial Future Development

Requirements
Must have
• Logos provided

```html
<!DOCTYPE html>
<html lang="en">
<head>
<meta charset="utf-8">
<title>712 35 Commerce Park – Trailer Banner</title>
<link rel="stylesheet" href="https://fonts.googleapis.com/css2?family=Poppins:wght@500;600&display=swap">
<style>
  :root {
    --page-bg: #f3f3f3;
    --panel-light: #e6e6e6;
    --panel-light-edge: #d9d9d9;
    --panel-dark: #000000;
    --band-dark: #333333;
    --ink: #222222;
    --white: #ffffff;
  }
  * { margin: 0; padding: 0; box-sizing: border-box; }
  html, body {
    width: 1200px;
    height: 899px;
    overflow: hidden;
    background: var(--page-bg);
    font-family: "Poppins", sans-serif;
  }
  .canvas {
    width: 1200px;
    height: 899px;
    display: flex;
    align-items: center;
    justify-content: center;
  }
  .banner {
    width: 1160px;
    height: 230px;
    display: flex;
    box-shadow: 0 6px 18px rgba(0,0,0,0.12);
  }
  .panel {
    position: relative;
    display: flex;
    flex-direction: column;
    align-items: center;
    justify-content: center;
  }
  .panel--side {
    background: linear-gradient(180deg, var(--panel-light) 0%, var(--panel-light-edge) 100%);
  }
  .panel--side::before,
  .panel--side::after {
    content: "";
    position: absolute;
    left: 0;
    right: 0;
    background: var(--band-dark);
  }
  .panel--side::before { top: 0; height: 10px; }
  .panel--side::after { bottom: 0; height: 9px; }
  .panel--developer { width: 380px; }
  .panel--project { width: 398px; background: var(--panel-dark); }
  .panel--builder { width: 382px; }

  .partner-name {
    font-weight: 600;
    color: var(--ink);
    line-height: 1.1;
    text-align: center;
    margin-top: 6px;
  }
  .panel--developer .partner-name { font-size: 34px; }
  .panel--builder .partner-name { font-size: 46px; }

  .web-address {
    font-weight: 500;
    font-size: 25px;
    color: var(--ink);
    margin-top: 26px;
  }

  .project-name {
    color: var(--white);
    font-weight: 600;
    text-align: center;
    line-height: 0.9;
  }
  .project-name__number {
    display: block;
    font-size: 80px;
    letter-spacing: 2px;
  }
  .project-name__label {
    display: block;
    font-size: 24px;
    font-weight: 500;
    letter-spacing: 2px;
    margin-top: 12px;
  }
</style>
</head>
<body>
<main class="canvas">
  <section class="banner" aria-label="712 35 Commerce Park highway trailer banner">
    <div class="panel panel--side panel--developer">
      <p class="partner-name">MERO DEVELOPMENT</p>
      <p class="web-address">Merodevelopments.com</p>
    </div>

    <div class="panel panel--project">
      <h1 class="project-name">
        <span class="project-name__number">712</span>
        <span class="project-name__number">35</span>
        <span class="project-name__label">COMMERCE PARK</span>
      </h1>
    </div>

    <div class="panel panel--side panel--builder">
      <p class="partner-name">RLW GROUP</p>
      <p class="web-address">Rlw.ca</p>
    </div>
  </section>
</main>
</body>
</html>
```